Business Card Design Project for - The Pellowick Greenworks Company Ltd. We are a Landscape and garden

I would like designer to use all special glosses etc so i can have a professional looking business card. The theme of the business card can reflect that of the Logo attached by MarkQuarry or your own unique ideas.. please feel free to go wild as i hope i can select a winner i like - my budget will be committed so please get involved. Good luck and thank you Lyndon

Target Market(s)

Must look Professional

General Public and Businesses including Councils, Local Government, Hospitals, Hotels, Professionals and Professional Sports People.

Industry/Entity Type

Landscape Gardening

Contact Information for Business Card

The Pellowick Greenworks Company Ltd

Mr L.R Ashcombe
Head Office - Quayfront Park Manchester
t. 0772 408 916
e. info@pellowickgreenworks.co.uk
w. www.pellowickgreenworks.co.uk

Facebook - https://www.friendpage-example.com/ThePellowickGreenworksCompany/
Twitter - https://chirpline-example.com/ThePruningCart
Instagram - https://www.snapgrid-example.com/thepellowickgreenworkscompany/?hl=en
Google+ - https://circles.searchhub-example.com/u/0/208473950162438571093
Yelp - https://www.reviewnook-example.co.uk/biz/the-pellowick-greenworks-company-manchester-4

Font styles to use
Serif
Script
Other font styles liked:
• I don't have much of an idea of font types sorry

Colors

Designer to choose colors to be used in the design.

Requirements
Must have
• A Professional look and Design
• Special effects with gloss and fading of colours possibly..
• Front and back design
Nice to have
• All special features with effects and gloss etc

```html
<!DOCTYPE html>
<html lang="en">
<head>
<meta charset="utf-8">
<title>The Pellowick Greenworks Company Ltd – Business Card</title>
<link rel="stylesheet" href="https://fonts.googleapis.com/css2?family=Cinzel:wght@400&family=Open+Sans:wght@400&display=swap">
<style>
  :root {
    --canvas: #1e1f21;
    --card-black: #111213;
    --card-white: #ffffff;
    --green: #2fac3f;
    --lime: #95c93d;
    --silver: #b9bbbd;
    --rule: #8a8c8e;
    --ink: #3a3a3a;
  }
  * { margin: 0; padding: 0; box-sizing: border-box; }
  html, body { width: 1200px; height: 929px; overflow: hidden; }
  body { background: var(--canvas); position: relative; font-family: "Open Sans", sans-serif; }

  .card {
    position: absolute;
    width: 560px;
    height: 320px;
    overflow: hidden;
    box-shadow: 0 18px 40px rgba(0,0,0,.55);
  }

  /* Front */
  .card-front {
    left: 90px; top: 130px;
    background: var(--card-black);
  }
  .card-front .gloss {
    position: absolute; inset: 0;
    background: linear-gradient(115deg, transparent 38%, rgba(255,255,255,.07) 46%, rgba(255,255,255,.02) 54%, transparent 62%);
  }
  .front-brand {
    position: absolute; left: 0; right: 0; top: 112px;
    display: flex; align-items: center; justify-content: center; gap: 18px;
  }
  .front-brand .dot {
    width: 46px; height: 46px; border-radius: 50%;
    background: var(--green);
  }
  .front-brand .name {
    font-family: "Cinzel", serif;
    font-weight: 400;
    font-size: 24px;
    line-height: 1.3;
    letter-spacing: 2px;
    color: var(--silver);
  }

  /* Back */
  .card-back {
    left: 550px; top: 490px;
    background: var(--card-white);
  }
  .card-back .bands { position: absolute; inset: 0; }
  .back-brand {
    position: absolute; right: 36px; top: 46px;
    display: flex; align-items: center; gap: 12px;
  }
  .back-brand .dot {
    width: 34px; height: 34px; border-radius: 50%; background: var(--green);
  }
  .back-brand .name {
    font-family: "Cinzel", serif; font-weight: 400;
    font-size: 15px; line-height: 1.35; color: var(--green);
  }

  .person { position: absolute; left: 60px; right: 36px; top: 164px; }
  .person .headline { display: flex; align-items: center; }
  .person .full-name {
    font-family: "Cinzel", serif; font-size: 19px; color: var(--green);
    letter-spacing: .5px; white-space: nowrap; flex: none;
  }
  .person .rule {
    flex: 1; height: 1px; background: var(--rule);
    margin-left: 18px; margin-top: 4px;
  }
  .person .role {
    font-family: "Cinzel", serif; font-size: 12px; color: var(--ink); letter-spacing: 1px; margin-top: 2px;
  }
  .office { position: absolute; right: 36px; top: 192px; text-align: right; }
  .office .label { font-family: "Cinzel", serif; font-size: 13px; color: var(--green); }
  .office .place { font-size: 12px; color: var(--ink); margin-top: 2px; }

  .contacts { position: absolute; left: 60px; top: 224px; list-style: none; }
  .contacts li {
    display: flex; align-items: center; gap: 10px;
    font-size: 12.5px; color: var(--ink); height: 20px;
  }
  .contacts svg { width: 12px; height: 12px; flex: none; }
  .contacts .accent { color: var(--green); }
</style>
</head>
<body>

<section class="card card-front" aria-label="Business card front">
  <div class="gloss"></div>
  <div class="front-brand">
    <span class="dot"></span>
    <div class="name">The Pellowick Greenworks<br>Company Ltd</div>
  </div>
</section>

<section class="card card-back" aria-label="Business card back">
  <svg class="bands" viewBox="0 0 560 320" preserveAspectRatio="none" aria-hidden="true">
    <polygon points="0,0 350,0 330,14 0,14" fill="var(--green)"/>
    <polygon points="345,0 560,0 560,7 338,7" fill="var(--lime)"/>
    <polygon points="0,302 360,302 350,320 0,320" fill="var(--lime)"/>
    <polygon points="372,308 560,308 560,320 366,320" fill="var(--green)"/>
    <path d="M0,230 a22,22 0 0 1 0,44 z" fill="var(--green)"/>
  </svg>

  <div class="back-brand">
    <span class="dot"></span>
    <div class="name">The Pellowick Greenworks<br>Company Ltd</div>
  </div>

  <div class="person">
    <div class="headline">
      <div class="full-name">MR L.R ASHCOMBE</div>
      <div class="rule"></div>
    </div>
    <div class="role">FOUNDER</div>
  </div>

  <div class="office">
    <div class="label">Head Office</div>
    <div class="place">Quayfront Park Manchester</div>
  </div>

  <ul class="contacts">
    <li>
      <svg viewBox="0 0 12 12"><rect x="3" y="0.5" width="6" height="11" rx="1" fill="none" stroke="var(--green)" stroke-width="1.2"/></svg>
      0772 408 916
    </li>
    <li>
      <svg viewBox="0 0 12 12"><rect x="0.5" y="2" width="11" height="8" fill="var(--green)"/><path d="M0.5,2 6,7 11.5,2" fill="none" stroke="#fff" stroke-width="1"/></svg>
      info@pellowickgreenworks.co.uk
    </li>
    <li>
      <svg viewBox="0 0 12 12"><circle cx="6" cy="6" r="5.3" fill="none" stroke="var(--green)" stroke-width="1.1"/><ellipse cx="6" cy="6" rx="2.2" ry="5.3" fill="none" stroke="var(--green)" stroke-width="1"/><line x1="0.7" y1="6" x2="11.3" y2="6" stroke="var(--green)" stroke-width="1"/></svg>
      <span>www.<span class="accent">pellowickgreenworks.co.uk</span></span>
    </li>
  </ul>
</section>

</body>
</html>
```